Indie musician needs album cover art

I am an independant musician releasing my second album via digital sources. I plan to make it available on Vendly and other digital stores but primarily distribute it free through Tunegrove.

The album's music style is a blend of singer-songwriter folk, punk, alt country, electronic rock and spoken word. The lyrical content is a dark journey through travel in foreign countries, relationships, airports and theatres, formed during my own journey as an audio engineer for a travelling theatre show.

The album is called "Ash Under Glass" - at times both a plea and a directive. I would like the album cover to reflect a sense of longing, restlessness, unease and movement. A subversive tone is also possible.

I have had a go at designing a couple of ideas myself, using my own photos. I like the ideas but I am not skilled in graphic design and am unable to take them further to get the right feel and look. I will post these as examples of tone. The finished work does not need to copy either of these.

A .zip of the album can be downloaded here (low fi mp3):

http://fylo.io/Qx7rT4

Target Market(s)

People who enjoy thoughtful, honest, homemade music. Definitely not a teeny pop audience. Adult, subversive, educated, emotional...

Industry/Entity Type

Graphic Design

Requirements
Must have
• Artist name (no caps): kipwren
Album name (prefer no caps): ash under glass

```html
<!DOCTYPE html>
<html lang="en">
<head>
<meta charset="utf-8">
<title>ash under glass — kipwren</title>
<link rel="stylesheet" href="https://fonts.googleapis.com/css2?family=Raleway:wght@100;200&display=swap">
<style>
  :root {
    --fog-light: #ccd2ca;
    --fog-mid: #b7bfb5;
    --fog-deep: #a3ab a1;
    --ground-dark: #5c6055;
    --ground-mid: #838169;
    --ground-sand: #e0d6b8;
    --horizon: #2b302d;
    --water-deep: #4f5a4b;
    --water-mid: #7f8c86;
    --water-light: #b9c4c6;
    --type: #f1f2ee;
  }
  html, body {
    margin: 0;
    padding: 0;
    width: 1200px;
    height: 1200px;
    overflow: hidden;
    background: var(--fog-mid);
  }
  .album-cover {
    position: relative;
    width: 1200px;
    height: 1200px;
    overflow: hidden;
    font-family: "Raleway", "Helvetica Neue", Arial, sans-serif;
  }
  .sky-photo {
    position: absolute;
    left: 0; top: 0;
    width: 1200px; height: 513px;
    background:
      radial-gradient(ellipse 900px 500px at 70% 15%, #dfe3dc 0%, rgba(223,227,220,0) 70%),
      linear-gradient(180deg, var(--fog-light) 0%, var(--fog-mid) 60%, #a8b0a6 100%);
  }
  .ground-photo {
    position: absolute;
    left: 0; top: 513px;
    width: 1200px; height: 687px;
    background: linear-gradient(180deg, var(--ground-dark) 0%, #6e705f 30%, var(--ground-mid) 55%, #b9b194 78%, var(--ground-sand) 100%);
  }
  .horizon-line {
    position: absolute;
    left: 0; top: 511px;
    width: 1200px; height: 3px;
    background: var(--horizon);
  }
  .water-disc {
    position: absolute;
    left: 265px; top: 145px;
    width: 710px; height: 725px;
    border-radius: 50%;
    background:
      repeating-linear-gradient(172deg, rgba(185,196,198,0.35) 0px, rgba(185,196,198,0) 28px, rgba(60,70,58,0.25) 56px),
      radial-gradient(circle at 50% 45%, var(--water-mid) 0%, #66705f 55%, var(--water-deep) 100%);
  }
  .album-title {
    position: absolute;
    left: 0; top: 458px;
    width: 1240px;
    margin: 0;
    text-align: center;
    font-weight: 100;
    font-size: 98px;
    line-height: 1;
    letter-spacing: -1px;
    color: var(--type);
  }
  .artist-name {
    position: absolute;
    left: 0; top: 592px;
    width: 1200px;
    margin: 0;
    text-align: center;
    font-weight: 200;
    font-size: 58px;
    line-height: 1;
    letter-spacing: 48px;
    color: var(--type);
    opacity: 0.9;
  }
</style>
</head>
<body>
  <main class="album-cover">
    <div class="sky-photo" role="img" aria-label="Misty aerial view of a coastline fading into fog"></div>
    <div class="ground-photo" role="img" aria-label="Inverted photograph of trees, a small house and a bird in flight against a pale sky"></div>
    <div class="horizon-line"></div>
    <div class="water-disc" role="img" aria-label="Circular close-up photograph of rippling water"></div>
    <h1 class="album-title">ash under glass</h1>
    <p class="artist-name">kipwren</p>
  </main>
</body>
</html>
```